Lone Elm Cattle Website

I need a website for my cattle company. I will be sharing pictures of my herd along with selling my calves individually. I need the following pages:
About
Cattle Sales
Bulls
Cows/Heifers
Gallery
Contact Us

I just uploaded a few pictures, but I have a lot more!

```html
<!DOCTYPE html>
<html lang="en">
<head>
<meta charset="utf-8">
<title>Lone Elm Cattle</title>
<link href="https://fonts.googleapis.com/css2?family=Bebas+Neue&family=Poppins:wght@400;500;600&display=swap" rel="stylesheet">
<style>
:root{
  --brown:#5a4029;
  --brown-dark:#3b2a1b;
  --ink:#2b2118;
  --text:#4a3d33;
  --line:#8a8580;
  --field:#d9d4cf;
  --white:#fff;
  --photo-grass:#6f7a45;
  --photo-dark:#3a2c22;
}
*{box-sizing:border-box;margin:0;padding:0}
html,body{width:1200px;height:5076px;overflow:hidden;background:var(--white);font-family:"Poppins",sans-serif;color:var(--text)}
.page{position:relative;width:1200px;height:5076px}
.abs{position:absolute}
.photo{position:absolute;border-radius:8px}
.wire{position:absolute;left:0;width:1200px;height:14px;border-top:2px solid var(--line);border-bottom:2px solid var(--line)}
.wire::after{content:"";position:absolute;left:0;right:0;top:5px;border-top:1px dashed var(--line)}
.btn{position:absolute;display:flex;align-items:center;justify-content:center;border-radius:22px;font-weight:600;font-size:14px;text-transform:uppercase}
.btn-solid{background:var(--brown);color:var(--white)}
.btn-outline{border:1.5px solid var(--white);color:var(--white)}
.title{font-family:"Bebas Neue",sans-serif;color:var(--brown);line-height:1}
.icon-mark{position:absolute;width:70px;height:78px;border-radius:10px;background:linear-gradient(#8b7564,#5a4029)}
.dash{display:inline-block;width:44px;height:2px;background:var(--brown);vertical-align:middle;position:relative}
.dash::after{content:"";position:absolute;right:-3px;top:-3px;width:8px;height:8px;border-radius:50%;background:var(--brown)}
.dash.l::after{left:-3px;right:auto}
.para{font-size:13px;line-height:24px;text-align:center}
/* header */
.nav a{position:absolute;top:64px;font-size:13px;color:var(--ink);text-decoration:none}
.logo-badge{position:absolute;left:510px;top:0;width:180px;height:178px;border-radius:0 0 90px 90px;background:var(--white);display:flex;flex-direction:column;align-items:center;justify-content:center}
.logo-badge .name{font-family:"Poppins",sans-serif;font-weight:600;font-size:17px;color:var(--brown);margin-top:40px}
/* cards */
.card{position:absolute;top:1900px;width:254px;height:410px;border-radius:10px;background:var(--white);box-shadow:0 2px 10px rgba(0,0,0,.12)}
.card .ph{position:absolute;left:6px;top:6px;width:242px;height:232px;border-radius:6px}
.card h3{position:absolute;left:22px;top:255px;font-size:16px;font-weight:600;color:var(--ink)}
.card p{position:absolute;left:22px;top:284px;width:215px;font-size:12.5px;line-height:20px}
.card .price{position:absolute;left:22px;top:331px;font-size:12px;font-weight:600;color:var(--ink)}
.card .buy{position:absolute;left:22px;top:365px;width:76px;height:20px;border-radius:10px;background:var(--brown);color:var(--white);font-size:10px;font-weight:600;display:flex;align-items:center;justify-content:center}
.arrow-btn{position:absolute;top:2080px;width:36px;height:36px;border-radius:50%;border:1px solid #ccc;background:var(--white);display:flex;align-items:center;justify-content:center}
/* form */
.field{position:absolute;border:1.5px solid var(--field);border-radius:4px;font-size:13px;color:#777;padding:24px 20px 0}
/* footer */
.footer{position:absolute;left:0;top:4670px;width:1200px;height:406px;background:var(--brown);color:var(--white)}
.footer h4{position:absolute;font-size:15px;font-weight:500;text-transform:uppercase}
.footer ul{position:absolute;list-style:none;font-size:13px;line-height:26px}
.footer li::before{content:"";display:inline-block;width:12px;height:12px;border-radius:3px;background:#c9bcae;margin-right:10px;vertical-align:-1px}
.f-ico{position:absolute;width:26px;height:26px;border:1px solid var(--white);border-radius:4px}
.f-ico svg{position:absolute;left:6px;top:6px}
.f-item{position:absolute;font-size:12.5px;line-height:16px}
</style>
</head>
<body>
<div class="page">

<!-- Header -->
<header>
  <nav class="nav">
    <a style="left:76px;font-weight:600;color:var(--brown)">Home</a>
    <a style="left:173px">About</a>
    <a style="left:268px">Cattle Sales</a>
    <a style="left:403px">Bulls</a>
    <a style="left:753px">Cows/Heifers</a>
    <a style="left:897px">Gallery</a>
  </nav>
  <div class="btn btn-solid" style="left:1001px;top:56px;width:124px;height:36px;font-size:13px;text-transform:none;font-weight:500">Contact Us</div>
</header>

<!-- Hero -->
<section>
  <div class="abs" role="img" aria-label="Highland cattle grazing on a grassy pasture" style="left:0;top:133px;width:1200px;height:718px;background:linear-gradient(100deg,#2c2620 0%,#4a4030 40%,#8a6a45 65%,#5f6b3a 100%)"></div>
  <div class="abs" style="left:0;top:326px;width:1200px;text-align:center;color:var(--white);font-size:19px;letter-spacing:.5px">WELCOME TO</div>
  <div class="abs title" style="left:0;top:362px;width:1200px;text-align:center;color:var(--white);font-size:88px;letter-spacing:4px">LONE ELM CATTLE</div>
  <div class="abs" style="left:0;top:462px;width:1200px;text-align:center;color:var(--white);font-size:19px;line-height:26px">Lorem ipsum dolor sit amet, consectetur adipiscing elit,<br>sed do eiusmod tempor incididunt ut labore et dolore</div>
  <div class="btn btn-outline" style="left:511px;top:543px;width:176px;height:44px;font-weight:500;font-size:16px">Contact Us</div>
  <div class="logo-badge"><span class="name">Lone Elm Cattle</span><span style="font-size:10px;color:var(--brown);font-weight:600">MILLBROOK, CA</span></div>
</section>
<div class="wire" style="top:843px"></div>

<!-- About -->
<section>
  <div class="abs" style="left:198px;top:1044px;width:268px;height:362px;border:1.5px solid var(--brown);border-radius:10px"></div>
  <div class="photo" role="img" aria-label="Dark Highland cow standing by water" style="left:123px;top:973px;width:268px;height:362px;background:linear-gradient(160deg,#6d8a4d,#3a2c22 60%,#6f7a45)"></div>
  <div class="photo" role="img" aria-label="Blonde Highland calf grazing" style="left:308px;top:1128px;width:270px;height:362px;background:linear-gradient(160deg,#4d5a33,#d8c59a 55%,#9b8a5a);border:5px solid var(--white)"></div>
  <div class="icon-mark" role="img" aria-label="Cattle emblem" style="left:680px;top:978px"></div>
  <h2 class="abs title" style="left:678px;top:1062px;font-size:62px">ABOUT US</h2>
  <div class="abs" style="left:678px;top:1125px;font-size:17px;color:var(--ink);font-family:Georgia,serif">WHO WE ARE <span class="dash" style="margin-left:6px"></span></div>
  <p class="abs" style="left:678px;top:1178px;width:434px;font-size:13px;line-height:25.5px">Lorem ipsum dolor sit amet, consectetur adipiscing elit, sed do eiu smod tempor incididunt ut labore et dolore magna aliqua. Quis ip sum suspendisse ultrices gravida. Risus commodo viverr a maecenas accumsan lacus vel facilisis. Lorem ipsum dolor sit amet, consectetur adipiscing elit, sed do eiusmod tempor incidid unt ut labore et dolore magna aliqua.</p>
  <div class="btn btn-solid" style="left:680px;top:1361px;width:160px;height:44px">Know More</div>
</section>
<div class="wire" style="top:1580px"></div>

<!-- Cattle Sales -->
<section>
  <div class="icon-mark" role="img" aria-label="Cattle emblem" style="left:565px;top:1625px"></div>
  <h2 class="abs title" style="left:0;top:1712px;width:1200px;text-align:center;font-size:62px"><span class="dash l" style="margin-right:18px"></span>CATTLE SALES<span class="dash" style="margin-left:18px"></span></h2>
  <p class="abs para" style="left:200px;top:1784px;width:800px;font-size:13px;line-height:21px">Lorem ipsum dolor sit amet, consectetur adipiscing elit, sed do eiusmod tempor incididunt ut labore et dolore magna aliqua. Quis ipsum suspendisse ultrices gravida. Risus commodo viverra maecenas accumsan lacus vel facilisis.</p>
  <div class="arrow-btn" style="left:20px"><svg width="10" height="10" viewBox="0 0 10 10"><path d="M6.5 1.5 3 5l3.5 3.5" fill="none" stroke="#333" stroke-width="1.5"/></svg></div>
  <div class="arrow-btn" style="left:1150px"><svg width="10" height="10" viewBox="0 0 10 10"><path d="M3.5 1.5 7 5 3.5 8.5" fill="none" stroke="#333" stroke-width="1.5"/></svg></div>
  <div class="card" style="left:68px"><div class="ph" role="img" aria-label="Red Highland calf in grass" style="background:linear-gradient(160deg,#7c8a55,#8a4a2a 55%,#6f7a45)"></div><h3>Cattle Name 1</h3><p>Lorem ipsum dolor sit amet, consectetur adipiscing elit</p><div class="price">$1000.00</div><div class="buy">BUY NOW</div></div>
  <div class="card" style="left:338px"><div class="ph" role="img" aria-label="Dark Highland cow in pasture" style="background:linear-gradient(160deg,#7c8a55,#3a2c22 55%,#6f7a45)"></div><h3>Cattle Name 2</h3><p>Lorem ipsum dolor sit amet, consectetur adipiscing elit</p><div class="price">$1000.00</div><div class="buy">BUY NOW</div></div>
  <div class="card" style="left:608px"><div class="ph" role="img" aria-label="Blonde Highland calf grazing" style="background:linear-gradient(160deg,#4d5a33,#d8c59a 55%,#9b8a5a)"></div><h3>Cattle Name 3</h3><p>Lorem ipsum dolor sit amet, consectetur adipiscing elit</p><div class="price">$1700.00</div><div class="buy">BUY NOW</div></div>
  <div class="card" style="left:878px"><div class="ph" role="img" aria-label="Black Highland cow by a fence" style="background:linear-gradient(160deg,#9aae7a,#1f1a16 55%,#5f6b3a)"></div><h3>Cattle Name 3</h3><p>Lorem ipsum dolor sit amet, consectetur adipiscing elit</p><div class="price">$1000.00</div><div class="buy">BUY NOW</div></div>
</section>

<!-- Bulls -->
<section>
  <div class="abs" role="img" aria-label="Red Highland bull lying in a fenced paddock" style="left:0;top:2440px;width:1200px;height:652px;background:linear-gradient(110deg,#9a8a6a 0%,#7a3a22 35%,#8a4a2a 55%,#6f7a45 100%)"></div>
  <div class="abs" style="left:880px;top:2440px;width:320px;height:652px;background:var(--white)"></div>
  <div class="abs" style="left:620px;top:2505px;width:530px;height:530px;border-radius:50%;background:var(--brown);box-shadow:0 0 0 18px rgba(90,64,41,.35)"></div>
  <div class="icon-mark" role="img" aria-label="Cattle emblem" style="left:850px;top:2555px;background:linear-gradient(#e8e0d6,#b8a898)"></div>
  <h2 class="abs title" style="left:620px;top:2640px;width:530px;text-align:center;color:var(--white);font-size:62px"><span class="dash l" style="margin-right:18px;background:#fff"></span>BULLS<span class="dash" style="margin-left:18px;background:#fff"></span></h2>
  <p class="abs para" style="left:660px;top:2722px;width:450px;color:var(--white);font-size:12.5px">Lorem ipsum dolor sit amet, consectetur adipiscing elit, sed do eiusmo d tempor incididunt ut labore et dolore magna aliqua. Quis ipsum suspendisse ultrices gravida. Risus commodo viverra maecen as accumsan lacus vel facilisis. Lorem ipsum dolor sit amet, consectetur adipiscing elit, sed do eiusmod tempor incidid unt ut labore et dolore magna aliqua. facilisis.</p>
  <div class="btn btn-outline" style="left:803px;top:2908px;width:160px;height:44px">Know More</div>
</section>
<div class="wire" style="top:2432px"></div>
<div class="wire" style="top:3090px"></div>

<!-- Gallery -->
<section>
  <div class="icon-mark" role="img" aria-label="Cattle emblem" style="left:565px;top:3137px"></div>
  <h2 class="abs title" style="left:0;top:3224px;width:1200px;text-align:center;font-size:62px"><span class="dash l" style="margin-right:18px"></span>OUR GALLERY<span class="dash" style="margin-left:18px"></span></h2>
  <p class="abs para" style="left:200px;top:3306px;width:800px;font-size:13px;line-height:21px">Lorem ipsum dolor sit amet, consectetur adipiscing elit, sed do eiusmod tempor incididunt ut labore et dolore magna aliqua. Quis ipsum suspendisse ultrices gravida. Risus commodo viverra maecenas accumsan lacus vel facilisis.</p>
  <div class="abs" role="img" aria-label="Blonde Highland calf grazing" style="left:68px;top:3400px;width:328px;height:208px;background:linear-gradient(160deg,#4d5a33,#d8c59a 55%,#9b8a5a)"></div>
  <div class="abs" role="img" aria-label="Red Highland calf in grass" style="left:68px;top:3618px;width:328px;height:208px;background:linear-gradient(160deg,#7c8a55,#8a4a2a 55%,#6f7a45)"></div>
  <div class="abs" role="img" aria-label="Dark Highland cow by water" style="left:410px;top:3400px;width:382px;height:426px;background:linear-gradient(160deg,#7c8a55,#3a2c22 55%,#6f7a45)"></div>
  <div class="abs" role="img" aria-label="Black Highland cow by a fence" style="left:805px;top:3400px;width:327px;height:208px;background:linear-gradient(160deg,#9aae7a,#1f1a16 55%,#5f6b3a)"></div>
  <div class="abs" role="img" aria-label="Two Highland cattle grazing" style="left:805px;top:3618px;width:327px;height:208px;background:linear-gradient(110deg,#2c2620,#4a4030 45%,#8a6a45 75%,#5f6b3a)"></div>
  <div class="abs" style="left:556px;top:3883px;width:8px;height:8px;border-radius:50%;background:var(--brown)"></div>
  <div class="abs" style="left:584px;top:3883px;width:8px;height:8px;border-radius:50%;background:#bbb"></div>
  <div class="abs" style="left:612px;top:3883px;width:8px;height:8px;border-radius:50%;background:#bbb"></div>
  <div class="abs" style="left:640px;top:3883px;width:8px;height:8px;border-radius:50%;background:#bbb"></div>
</section>
<div class="wire" style="top:3980px"></div>

<!-- Contact -->
<section>
  <div class="photo" role="img" aria-label="Black Highland cow behind a wire fence" style="left:128px;top:4105px;width:362px;height:410px;border-radius:14px;background:linear-gradient(160deg,#9aae7a,#1f1a16 55%,#5f6b3a)"></div>
  <div class="icon-mark" role="img" aria-label="Cattle emblem" style="left:598px;top:4035px"></div>
  <h2 class="abs title" style="left:593px;top:4122px;font-size:62px">CONTACT US <span class="dash" style="margin-left:14px"></span></h2>
  <p class="abs" style="left:593px;top:4197px;width:540px;font-size:12.5px;line-height:20px">Lorem ipsum dolor sit amet, consectetur adipiscing elit, sed do eiusmod tempor incididunt ut labore et dolore magna aliqua. Quis ipsum suspendisse ultrices</p>
  <div class="field" style="left:600px;top:4273px;width:251px;height:48px;padding-top:14px">Your Name</div>
  <div class="field" style="left:868px;top:4273px;width:251px;height:48px;padding-top:12px">Phone Number</div>
  <div class="field" style="left:600px;top:4332px;width:519px;height:48px;padding-top:14px">Email Address</div>
  <div class="field" style="left:600px;top:4392px;width:519px;height:78px;padding-top:16px">Message</div>
  <div class="btn btn-solid" style="left:607px;top:4515px;width:130px;height:40px">Submit</div>
</section>
<div class="wire" style="top:4655px"></div>

<!-- Footer -->
<footer class="footer">
  <div class="abs" style="left:118px;top:112px;width:160px;height:160px;border-radius:50%;border:2px solid var(--white)"></div>
  <div class="abs" style="left:60px;top:212px;width:280px;text-align:center;font-weight:600;font-size:24px;background:var(--brown)">Lone Elm Cattle</div>
  <div class="abs" style="left:60px;top:252px;width:280px;text-align:center;font-size:11px;font-weight:600">MILLBROOK, CA</div>

  <h4 style="left:412px;top:100px">Quick Links</h4>
  <div class="abs" style="left:412px;top:128px;width:40px;height:2px;background:#fff"></div>
  <ul style="left:412px;top:144px"><li>About</li><li>Cattle Sales</li><li>Bulls</li><li>Cows/Heifers</li><li>Gallery</li><li>Contact Us</li></ul>

  <h4 style="left:626px;top:104px">Contact Us</h4>
  <div class="abs" style="left:626px;top:132px;width:40px;height:2px;background:#fff"></div>
  <div class="f-ico" style="left:626px;top:162px"><svg width="14" height="14" viewBox="0 0 14 14"><path d="M3 1h2l1 3-1.5 1a7 7 0 0 0 4.5 4.5L10 8l3 1v2a2 2 0 0 1-2 2A10 10 0 0 1 1 3a2 2 0 0 1 2-2z" fill="none" stroke="#fff" stroke-width="1.2"/></svg></div>
  <div class="f-item" style="left:670px;top:162px">CALL US<br>8012 345 6789</div>
  <div class="f-ico" style="left:626px;top:214px"><svg width="14" height="14" viewBox="0 0 14 14"><rect x="1" y="3" width="12" height="8" fill="none" stroke="#fff" stroke-width="1.2"/><path d="M1 3l6 5 6-5" fill="none" stroke="#fff" stroke-width="1.2"/></svg></div>
  <div class="f-item" style="left:670px;top:214px">EMAIL US<br>info@websitename.com</div>
  <div class="f-ico" style="left:626px;top:266px"><svg width="14" height="14" viewBox="0 0 14 14"><path d="M7 13s-4-4.5-4-7.5a4 4 0 0 1 8 0C11 8.5 7 13 7 13z" fill="none" stroke="#fff" stroke-width="1.2"/><circle cx="7" cy="5.5" r="1.4" fill="#fff"/></svg></div>
  <div class="f-item" style="left:670px;top:266px">Address line Dummy Here<br>Address line Here</div>

  <h4 style="left:900px;top:100px">Newsletter Sign Up</h4>
  <div class="abs" style="left:900px;top:128px;width:40px;height:2px;background:#fff"></div>
  <p class="abs" style="left:905px;top:172px;width:180px;font-size:12.5px;line-height:17px">Subscribe our newsletter to get the latest news.</p>
  <div class="abs" style="left:898px;top:227px;width:202px;height:32px;border:1px solid #fff;border-radius:16px;font-size:11px;padding:8px 16px">Enter Email Address</div>
  <div class="abs" style="left:1068px;top:232px;width:22px;height:22px;border:1px solid #fff;border-radius:50%"><svg width="20" height="20" viewBox="0 0 20 20"><path d="M5 10h10M11 6l4 4-4 4" fill="none" stroke="#fff" stroke-width="1.3"/></svg></div>

  <div class="abs" style="left:0;top:350px;width:1200px;height:1px;background:rgba(255,255,255,.3)"></div>
  <div class="abs" style="left:72px;top:368px;font-size:12.5px">Copyright © 2025 All Rights Reserved By Company name</div>
  <div class="abs" style="left:1052px;top:364px;width:30px;height:30px;border:1.5px solid #fff;border-radius:50%"></div>
  <div class="abs" style="left:1096px;top:364px;width:30px;height:30px;border:1.5px solid #fff;border-radius:50%"></div>
</footer>

</div>
</body>
</html>
```